Wrenfield Atelier, and interior design project management company!

We invite you to participate in our logo and web design contest for "Wrenfield Atelier Management Corp."!

Here's a brief description of our company paraphrased by ChatGPT.

Company Overview:
Wrenfield Atelier Management Corp. is your trusted partner for interior design project management, guided by international standards set forth by the Ordway Planning Council (OPC) and the Structured Delivery Reference Compendium (SDREF). With a commitment to excellence, we seamlessly merge modern project management techniques with traditional values, emphasizing quality and attention to detail in every project.

Our Unique Strengths:

Local Fabrication Facility: What sets us apart is our in-house fabrication facility, a millwork shop with an impressive 20 years of experience. This facility empowers us to exercise meticulous control over the production process, ensuring that your project is crafted with precision and care right in our local community.

Experienced Skilled Workers: At Wrenfield Atelier Management Corp., our team comprises highly skilled and experienced craftsmen and artisans. They bring years of expertise to every project, guaranteeing that your interior design visions are brought to life with unmatched skill and finesse.

Serving Commercial and Residential Clients:
Our primary focus is on serving commercial clients, specializing in Tenant Improvement (TI) projects. We understand the unique demands of commercial spaces, and our project management expertise ensures that your commercial interior design projects are executed efficiently and within budget.

In addition to our commercial expertise, we also cater to discerning residential clients who seek that extra level of attention to detail. Our comprehensive services encompass all types of projects, from commercial tenant improvements to residential renovations. Regardless of the project's scale or scope, you can trust that all aspects will be managed seamlessly by our professional team.

Why Choose Us:
We are not just project managers; we are passionate advocates for your project's success. By adhering to OPC and SDREF standards, we deliver project management that is structured, efficient, and dependable. Our commitment to personal and approachable service, combined with our dedication to quality craftsmanship, ensures that your interior design projects are executed flawlessly from start to finish.

With Wrenfield Atelier Management Corp., you can trust that your project will benefit from the perfect blend of modern project management techniques and traditional values, resulting in interiors that are not only aesthetically pleasing but also built to stand the test of time.

Whether you require a commercial TI project or a residential project with meticulous attention to detail, we are the one-stop professional company that can bring your vision to life. Join our logo design contest, and let's together represent our dedication to excellence in project management and craftsmanship for both commercial and residential clients.

Target Market(s)

interior designers and architects, business owners

Industry/Entity Type

construction, project management, interior design, custom millwork and cabinets

Number of Pages Required

1 page

Requirements
Must have
• General consideration for design to float from social media to website.
Nice to have
• Consideration for more sophisticated backend support for customer support and project management update integrations apps such as ClickUp. (Technical portion not part of scope of work.)

```html
<!DOCTYPE html>
<html lang="en">
<head>
<meta charset="utf-8">
<title>Wrenfield Atelier Management Corp.</title>
<link href="https://fonts.googleapis.com/css2?family=Bebas+Neue&family=Roboto:wght@400;500;700&display=swap" rel="stylesheet">
<style>
:root{
  --gold:#d9a13b;
  --gold-light:#e7b860;
  --dark:#2b2b2b;
  --footer:#2f2f2f;
  --grey-bg:#f4f4f4;
  --text:#555;
  --heading:#222;
  --steel:#7a7a7a;
  --white:#fff;
}
*{box-sizing:border-box;margin:0;padding:0}
html,body{width:1200px;height:4612px;overflow:hidden}
body{position:relative;font-family:'Roboto',sans-serif;color:var(--text);background:var(--white)}
.abs{position:absolute}
.display{font-family:'Bebas Neue',sans-serif;font-weight:400;letter-spacing:.5px;color:var(--heading)}
.display .accent{color:var(--gold)}
.btn{position:absolute;display:flex;align-items:center;justify-content:center;font-size:13px;font-weight:500;text-transform:uppercase;color:var(--white)}
.btn-gold{background:var(--gold)}
.btn-ghost{border:2px solid rgba(255,255,255,.9);background:rgba(0,0,0,.25)}
p{line-height:1.75}

/* top bar */
.topbar{left:0;top:0;width:1200px;height:45px;background:var(--dark);color:#ddd;font-size:13px}
.topbar .item{position:absolute;top:15px;display:flex;align-items:center;gap:8px}
.social{position:absolute;width:28px;height:28px;border-radius:50%}
.topbar .social{top:8px;background:var(--white)}

/* nav */
.nav{left:0;top:45px;width:1200px;height:80px;background:var(--white);border-bottom:1px solid #e6e6e6}
.nav a{position:absolute;top:0;height:80px;display:flex;align-items:center;font-size:14px;font-weight:500;color:var(--heading);text-decoration:none;text-transform:uppercase}
.nav .sep{position:absolute;top:0;width:1px;height:80px;background:#e5e5e5}
.nav .active{color:var(--gold)}
.nav .contact{left:935px;width:152px;justify-content:center;background:var(--gold);color:var(--white)}
.brandbox{left:507px;top:0;width:186px;height:200px;z-index:5}
.brand-name{position:absolute;left:0;top:74px;width:186px;text-align:center;font-family:'Bebas Neue',sans-serif;font-size:23px;color:var(--dark);line-height:1}
.brand-sub{position:absolute;left:0;top:100px;width:186px;text-align:center;font-size:8px;letter-spacing:1.5px;color:var(--steel)}
.brand-mark{position:absolute;left:75px;top:22px;width:36px;height:36px;background:var(--gold)}

/* hero */
.hero{left:0;top:125px;width:1200px;height:708px}
.hero-title{position:absolute;top:278px;width:600px;text-align:center;font-family:'Bebas Neue',sans-serif;font-size:46px;color:var(--white)}

/* about */
.about-text{left:636px;top:975px;width:452px}
.about-text h2{font-size:44px;margin-bottom:18px}
.about-text p{font-size:14.5px;text-align:justify;margin-bottom:12px}

/* strengths */
.strengths{left:0;top:1544px;width:1200px;height:820px;background:var(--grey-bg)}
.section-title{position:absolute;left:0;width:1200px;text-align:center;font-size:46px}
.strengths .lead{position:absolute;left:170px;top:138px;width:860px;text-align:center;font-size:15px;line-height:1.95}
.card{position:absolute;top:336px;width:304px;height:403px;background:var(--white);border:3px solid var(--steel);text-align:center}
.card.gold{border-color:var(--gold)}
.card .hex{position:absolute;left:107px;top:-50px}
.card h3{margin-top:74px;font-size:16px;font-weight:700;color:var(--heading);line-height:1.65;text-transform:uppercase;padding:0 30px}
.card p{margin-top:18px;font-size:14px;line-height:1.85;padding:0 14px}

/* services */
.services{left:0;top:2364px;width:1200px;height:691px;background:linear-gradient(120deg,#d99a2c 0%,#e4b054 55%,#efc06a 100%)}
.services .section-title{top:66px;color:var(--white)}
.tab{position:absolute;top:149px;height:44px;display:flex;align-items:center;justify-content:center;font-size:13px;font-weight:500}
.tab.on{left:462px;width:133px;background:var(--white);color:var(--heading)}
.tab.off{left:605px;width:133px;border:2px solid var(--white);color:var(--white)}
.svc{position:absolute;top:238px;width:473px;height:378px;background:var(--white)}
.svc .ph{position:absolute;left:7px;top:7px;width:459px;height:290px}
.svc h3{position:absolute;left:0;top:318px;width:100%;text-align:center;font-size:17px;font-weight:500;color:var(--heading)}

/* why */
.why-text{left:111px;top:3200px;width:433px}
.why-text h2{font-size:44px;margin-bottom:20px}
.why-text p{font-size:14.5px;text-align:justify;margin-bottom:14px}

/* testimonials */
.quote{position:absolute;top:3877px;width:304px;height:274px;background:var(--white);box-shadow:0 2px 14px rgba(0,0,0,.09);padding:26px 22px}
.stars{color:var(--gold);font-size:15px;letter-spacing:2px}
.quote p{margin-top:12px;font-size:14px;line-height:1.95;color:#444;border-bottom:1px solid #ddd;padding-bottom:12px}
.person{display:flex;align-items:center;gap:18px;margin-top:16px}
.avatar{width:56px;height:56px;border-radius:50%;background:linear-gradient(135deg,#cfc6bd,#9c8f84)}
.person b{display:block;font-size:13px;color:var(--heading);font-weight:700}
.person span{font-size:11px;color:#555}
.arrow{position:absolute;top:3999px;width:34px;height:34px;border-radius:50%}

/* footer */
.footer{left:0;top:4236px;width:1200px;height:376px;background:var(--footer);color:#e8e8e8}
.footer .col{position:absolute;top:70px}
.footer h4{font-size:19px;font-weight:500;margin-bottom:16px;color:var(--white)}
.footer li{list-style:none;font-size:13px;margin-bottom:21px}
.footer .contact b{display:block;font-size:15px;font-weight:500;margin-bottom:4px}
.footer .contact div{font-size:11px;line-height:1.5;margin-bottom:12px}
.footer .rule{position:absolute;left:111px;top:313px;width:976px;height:1px;background:#555}
.footer .legal{position:absolute;left:0;top:336px;width:1200px;text-align:center;font-size:12px}
.footer .social{top:328px;background:var(--gold);width:26px;height:26px}
.footer .social.ring{background:none;border:2px solid #ddd}
</style>
</head>
<body>

<!-- Top bar -->
<div class="abs topbar">
  <div class="item" style="left:111px">
    <svg width="12" height="12" viewBox="0 0 24 24"><path fill="#d9a13b" d="M6.6 10.8a15 15 0 0 0 6.6 6.6l2.2-2.2c.3-.3.7-.4 1-.2 1.1.4 2.3.6 3.6.6.6 0 1 .4 1 1V20c0 .6-.4 1-1 1A17 17 0 0 1 3 4c0-.6.4-1 1-1h3.5c.6 0 1 .4 1 1 0 1.3.2 2.5.6 3.6.1.3 0 .7-.2 1z"/></svg>
    +1 (555) 014 2290
  </div>
  <div class="item" style="left:256px">
    <svg width="13" height="10" viewBox="0 0 26 20"><rect width="26" height="20" rx="2" fill="#d9a13b"/><path d="M1 2l12 9 12-9" stroke="#2b2b2b" stroke-width="2" fill="none"/></svg>
    hello@wrenfieldatelier.com
  </div>
  <span class="social" style="left:971px"></span>
  <span class="social" style="left:1005px"></span>
  <span class="social" style="left:1039px"></span>
</div>

<!-- Navigation -->
<div class="abs nav">
  <a class="active" style="left:111px">Home</a>
  <span class="sep" style="left:174px"></span>
  <a style="left:193px">About Us</a>
  <span class="sep" style="left:285px"></span>
  <a style="left:304px">Our Services</a>
  <a style="left:799px">Our Project</a>
  <a class="contact">Contact Us</a>
</div>
<div class="abs brandbox">
  <svg width="186" height="200" viewBox="0 0 186 200" style="position:absolute;left:0;top:0">
    <polygon points="0,0 186,0 186,148 93,200 0,148" fill="#fff"/>
  </svg>
  <span class="brand-mark"></span>
  <div class="brand-name">Wrenfield Atelier</div>
  <div class="brand-sub">MANAGEMENT CORP</div>
</div>

<!-- Hero -->
<div class="abs hero">
  <svg width="1200" height="708" viewBox="0 0 1200 708" style="position:absolute;left:0;top:0">
    <defs>
      <linearGradient id="office" x1="0" y1="0" x2="1" y2="1"><stop offset="0" stop-color="#5a4a3c"/><stop offset=".5" stop-color="#3d3a36"/><stop offset="1" stop-color="#6e6559"/></linearGradient>
      <linearGradient id="bedroom" x1="0" y1="0" x2="1" y2="1"><stop offset="0" stop-color="#a8a29a"/><stop offset=".55" stop-color="#8b877f"/><stop offset="1" stop-color="#6f6a63"/></linearGradient>
      <linearGradient id="goldband" x1="0" y1="0" x2="1" y2="0"><stop offset="0" stop-color="#d39b34"/><stop offset="1" stop-color="#e8b75c"/></linearGradient>
    </defs>
    <polygon points="0,500 1200,500 1200,548 600,708 0,548" fill="url(#goldband)"/>
    <polygon points="0,0 600,0 600,690 0,540" fill="url(#office)" role="img" aria-label="Photo of an open-plan commercial office interior"/>
    <polygon points="600,0 1200,0 1200,540 600,690" fill="url(#bedroom)" role="img" aria-label="Photo of a calm residential bedroom interior"/>
  </svg>
  <div class="hero-title" style="left:0">Commercial Project</div>
  <div class="hero-title" style="left:600px">Residential Project</div>
  <div class="btn btn-ghost" style="left:233px;top:353px;width:132px;height:44px">Learn More</div>
  <div class="btn btn-ghost" style="left:833px;top:353px;width:132px;height:44px">Learn More</div>
</div>

<!-- About -->
<svg class="abs" style="left:111px;top:887px" width="485" height="554" viewBox="0 0 485 554">
  <defs><linearGradient id="aboutph" x1="0" y1="0" x2="1" y2="1"><stop offset="0" stop-color="#d9d3cc"/><stop offset=".5" stop-color="#8e4a55"/><stop offset="1" stop-color="#b7aea5"/></linearGradient></defs>
  <polygon points="249,14 485,149 485,419 249,554 14,419 14,149" fill="none" stroke="#d9a13b" stroke-width="4"/>
  <polygon points="235,0 471,135 471,405 235,540 0,405 0,135" fill="url(#aboutph)" role="img" aria-label="Photo of a project manager with a tablet and his team"/>
</svg>
<div class="abs about-text">
  <h2 class="display">About <span class="accent">Us</span></h2>
  <p>Wrenfield Atelier Management Corp. is your trusted partner for interior design project management, guided by international standards set forth by the Ordway Planning Council (OPC) and the Structured Delivery Reference Compendium (SDREF).</p>
  <p>With a commitment to excellence, we seamlessly merge modern project management techniques with traditional values, emphasizing quality and attention to detail in every project.</p>
</div>
<div class="btn btn-gold" style="left:636px;top:1285px;width:130px;height:46px">Learn More</div>

<!-- Strengths -->
<div class="abs strengths">
  <h2 class="display section-title" style="top:72px">Our Unique <span class="accent">Strengths</span></h2>
  <p class="lead">In addition to our commercial expertise, we also cater to discerning residential clients who seek that extra level of attention to detail. Our comprehensive services encompass all types of projects, from commercial tenant improvements to residential renovations. Regardless of the project's scale or scope, you can trust that all aspects will be managed seamlessly by our professional team.</p>

  <div class="card" style="left:111px">
    <svg class="hex" width="90" height="96" viewBox="0 0 90 96"><polygon points="45,0 90,24 90,72 45,96 0,72 0,24" fill="#7a7a7a"/><rect x="30" y="30" width="22" height="34" fill="none" stroke="#fff" stroke-width="3"/><circle cx="58" cy="60" r="8" fill="#fff"/><circle cx="58" cy="60" r="3" fill="#7a7a7a"/></svg>
    <h3>Local Fabrication Facility</h3>
    <p>What sets us apart is our in-house fabrication facility, a millwork shop with an impressive 20 years of experience. This facility empowers us to exercise meticulous control over the production process, ensuring that your project is crafted with precision and care right in our local community.</p>
  </div>
  <div class="card gold" style="left:448px">
    <svg class="hex" width="90" height="96" viewBox="0 0 90 96"><polygon points="45,0 90,24 90,72 45,96 0,72 0,24" fill="#d9a13b"/><circle cx="45" cy="32" r="7" fill="#fff"/><path d="M33 56a12 12 0 0 1 24 0z" fill="#fff"/><text x="45" y="70" text-anchor="middle" fill="#fff" font-size="11">★★★</text></svg>
    <h3>Experienced Skilled Workers</h3>
    <p>At Wrenfield Atelier Management Corp., our team comprises highly skilled and experienced craftsmen and artisans. They bring years of expertise to every project, guaranteeing that your interior design visions are brought to life with unmatched skill and finesse.</p>
  </div>
  <div class="card" style="left:784px">
    <svg class="hex" width="90" height="96" viewBox="0 0 90 96"><polygon points="45,0 90,24 90,72 45,96 0,72 0,24" fill="#7a7a7a"/><circle cx="36" cy="34" r="5" fill="#fff"/><circle cx="54" cy="34" r="5" fill="#fff"/><path d="M26 50a10 8 0 0 1 20 0zM44 50a10 8 0 0 1 20 0z" fill="#fff"/><path d="M24 64h20l8-6h12" stroke="#fff" stroke-width="4" fill="none" stroke-linecap="round"/></svg>
    <h3>Serving Commercial &amp; Residential Clients</h3>
    <p>Our primary focus is on serving commercial clients, specializing in Tenant Improvement (TI) projects. We understand the unique demands of commercial spaces, and our project management expertise ensures that your commercial interior design projects are executed efficiently and within budget.</p>
  </div>
</div>

<!-- Services -->
<div class="abs services">
  <h2 class="display section-title">Services</h2>
  <div class="tab on">COMMERCIAL</div>
  <div class="tab off">RESIDENTIAL</div>
  <div class="svc" style="left:111px">
    <div class="ph" role="img" aria-label="Photo of engineers reviewing plans on a commercial site" style="background:linear-gradient(135deg,#e8ebee,#c8ccd0 60%,#8d8f88)"></div>
    <h3>PROJECT MANAGEMENT</h3>
  </div>
  <div class="svc" style="left:616px">
    <div class="ph" role="img" aria-label="Photo of craftsmen working together in a workshop" style="background:linear-gradient(135deg,#a6896c,#c9b49a 55%,#6d5c4c)"></div>
    <h3>CRAFTSMANSHIP</h3>
  </div>
</div>

<!-- Why choose us -->
<div class="abs why-text">
  <h2 class="display">Why Choose <span class="accent">Us</span></h2>
  <p>We are not just project managers; we are passionate advocates for your project's success. By adhering to OPC and SDREF standards, we deliver project management that is structured, efficient, and dependable.</p>
  <p>Our commitment to personal and approachable service, combined with our dedication to quality craftsmanship, ensures that your interior design projects are executed flawlessly from start to finish.</p>
</div>
<div class="btn btn-gold" style="left:111px;top:3539px;width:130px;height:46px">Learn More</div>
<div class="abs" role="img" aria-label="Photo of a dining room with sage walls, wooden table and pendant lamp" style="left:600px;top:3166px;width:487px;height:428px;background:linear-gradient(135deg,#9eb2a2,#c9cfc2 50%,#7a6149)"></div>

<!-- Testimonials -->
<h2 class="abs display section-title" style="top:3785px">What Our <span class="accent">Clients Say</span></h2>
<svg class="arrow" style="left:33px" viewBox="0 0 34 34"><circle cx="17" cy="17" r="17" fill="#ddd"/><path d="M20 10l-7 7 7 7" stroke="#333" stroke-width="2" fill="none"/></svg>
<svg class="arrow" style="left:1129px" viewBox="0 0 34 34"><circle cx="17" cy="17" r="17" fill="#d9a13b"/><path d="M14 10l7 7-7 7" stroke="#fff" stroke-width="2" fill="none"/></svg>
<div class="quote" style="left:111px">
  <div class="stars">★★★★★</div>
  <p>Lorem ipsum dolor sit amet, consecte adipiscing elit, sed do eiusmod tempo incididunt ut labore et dolore magna aliqua ut enim ad minim.</p>
  <div class="person"><span class="avatar" role="img" aria-label="Client portrait"></span><div><b>DANA WHITLOCK</b><span>Unites States</span></div></div>
</div>
<div class="quote" style="left:448px">
  <div class="stars">★★★★★</div>
  <p>Lorem ipsum dolor sit amet, consecte adipiscing elit, sed do eiusmod tempo incididunt ut labore et dolore magna aliqua ut enim ad minim.</p>
  <div class="person"><span class="avatar" role="img" aria-label="Client portrait"></span><div><b>DANA WHITLOCK</b><span>Unites States</span></div></div>
</div>
<div class="quote" style="left:784px">
  <div class="stars">★★★★★</div>
  <p>Lorem ipsum dolor sit amet, consecte adipiscing elit, sed do eiusmod tempo incididunt ut labore et dolore magna aliqua ut enim ad minim.</p>
  <div class="person"><span class="avatar" role="img" aria-label="Client portrait"></span><div><b>DANA WHITLOCK</b><span>Unites States</span></div></div>
</div>

<!-- Footer -->
<div class="abs footer">
  <span class="abs" style="left:170px;top:100px;width:54px;height:54px;background:var(--gold)"></span>
  <div class="abs" style="left:80px;top:172px;width:234px;text-align:center;font-family:'Bebas Neue',sans-serif;font-size:28px;color:var(--gold)">Wrenfield Atelier</div>
  <div class="abs" style="left:80px;top:205px;width:234px;text-align:center;font-size:9px;letter-spacing:2px;color:var(--steel)">MANAGEMENT CORP</div>

  <div class="col" style="left:421px">
    <h4>Quick Links</h4>
    <ul><li>Home</li><li>About Us</li><li>Our Services</li><li>Our Projects</li><li>Contact Us</li></ul>
  </div>
  <div class="col" style="left:645px">
    <h4>Support</h4>
    <ul><li>Privacy Policy</li><li>Terms And Conditions</li><li>Sitemap</li></ul>
  </div>
  <div class="col contact" style="left:899px">
    <h4>Contact Info</h4>
    <b>Address:</b><div>212 Marlow Lane, Suite 4,<br>United States</div>
    <b>Phone:</b><div>+1 (555) 014 2290</div>
    <b>Email:</b><div>hello@wrenfieldatelier.com</div>
  </div>

  <div class="rule"></div>
  <div class="legal">© 2023 <b>WRENFIELD ATELIER MANAGEMENT CORP</b> &nbsp;|&nbsp; All Rights Reserved</div>
  <span class="social" style="left:992px"></span>
  <span class="social ring" style="left:1026px"></span>
  <span class="social ring" style="left:1060px"></span>
</div>

</body>
</html>
```